Business Card Design for an Investment Company

We need a business card design for our private investment company, called Ashbourne Partners. Ashbourne Partners is an investments partnership that aims to acquire shares in listed companies with a view to influencing those companies through active dialogue in order to improve their value. We need designs that use the logo colors (blue, grey, white), we need both English and Arabic on the business cards (can be on one side or 2 sides). The final logo should communicate professionalism, conservatism (nothing too fancy or too cheesy), that we are smart, conservative and old school.

Target Market(s)

Investment companies

Industry/Entity Type

Investment

Contact Information for Business Card

Khalid Yousef Rumaithi
Senior Executive Officer

Palm Terrace 07, Level 3, Office 215/12
HLMZ

+9714987650
krumaithi@ashbournepartners.com
www.ashbournepartners.com

Requirements
Must have
• Logo to be placed on the left hand side of the business card
• for the Arabic, we only need to have the name and title so it can be accomodated on one side so we can have the other side with full color and logo. The arabic that needs to be used is the below:
• خالد يوسف الرميثي
• المدير التنفيدي

```html
<!DOCTYPE html>
<html lang="en">
<head>
<meta charset="utf-8">
<title>Ashbourne Partners – Business Card</title>
<link href="https://fonts.googleapis.com/css2?family=Noto+Naskh+Arabic:wght@500;700&family=Roboto:wght@400;500;700&display=swap" rel="stylesheet">
<style>
  :root{
    --brand-blue:#1a6ea8;
    --brand-blue-dark:#125a8c;
    --charcoal:#3a3b3e;
    --charcoal-deep:#232426;
    --grey-mark:#5a5b5e;
    --paper:#ffffff;
    --paper-shade:#e9eaec;
    --ink-light:#d6d7d9;
    --stage:#d9dbde;
  }
  *{box-sizing:border-box;margin:0;padding:0}
  html,body{width:1200px;height:997px;overflow:hidden}
  body{
    background:var(--stage);
    font-family:"Roboto",Arial,sans-serif;
    display:flex;align-items:center;justify-content:center;gap:40px;
  }
  .card{
    position:relative;width:560px;height:320px;border-radius:24px;overflow:hidden;
    box-shadow:0 10px 28px rgba(0,0,0,.18);
  }
  .card-front{background:linear-gradient(135deg,var(--paper) 0%,var(--paper) 55%,var(--paper-shade) 100%)}
  .card-back{background:var(--charcoal)}
  .card-art{position:absolute;inset:0;width:100%;height:100%}

  .wordmark{
    position:absolute;display:flex;align-items:center;gap:10px;
    color:var(--brand-blue);font-weight:700;white-space:nowrap;letter-spacing:-.5px;
  }
  .wordmark-square{display:block;background:var(--grey-mark)}
  .card-front .wordmark{left:44px;top:50%;transform:translateY(-50%);font-size:40px}
  .card-front .wordmark-square{width:22px;height:22px}
  .card-back .wordmark{left:36px;top:58px;font-size:34px}
  .card-back .wordmark-square{width:18px;height:18px}

  .holder{position:absolute;left:170px;width:290px;top:148px;text-align:center;line-height:1.15}
  .holder-name{color:var(--paper);font-weight:700;font-size:16px;letter-spacing:.6px}
  .holder-title{color:var(--charcoal-deep);font-weight:500;font-size:14px}

  .holder-arabic{
    position:absolute;right:30px;top:206px;text-align:right;
    font-family:"Noto Naskh Arabic","Roboto",serif;line-height:1.35;
  }
  .holder-arabic-name{color:var(--paper);font-weight:700;font-size:17px}
  .holder-arabic-title{color:var(--ink-light);font-weight:500;font-size:14px}

  .website{position:absolute;right:30px;top:284px;color:var(--brand-blue);font-weight:700;font-size:14px;letter-spacing:.3px}

  .contacts{position:absolute;left:28px;top:210px;list-style:none;color:var(--ink-light);font-size:13px;line-height:1.25}
  .contacts li{display:flex;align-items:flex-start;gap:10px;margin-bottom:6px}
  .contact-icon{flex:none;width:16px;height:16px}
</style>
</head>
<body>

  <section class="card card-front" aria-label="Card front">
    <div class="wordmark"><span class="wordmark-square"></span>Ashbourne Partners</div>
  </section>

  <section class="card card-back" aria-label="Card back">
    <svg class="card-art" viewBox="0 0 560 320" aria-hidden="true">
      <rect x="0" y="0" width="560" height="175" fill="var(--paper)"/>
      <polygon points="0,168 560,150 560,158 0,176" fill="var(--brand-blue)"/>
      <polygon points="150,200 185,142 445,134 480,160 470,188" fill="var(--brand-blue)"/>
      <polygon points="445,134 480,160 560,150 560,148" fill="var(--brand-blue-dark)"/>
    </svg>

    <div class="wordmark"><span class="wordmark-square"></span>Ashbourne Partners</div>

    <div class="holder">
      <p class="holder-name">KHALID YOUSEF RUMAITHI</p>
      <p class="holder-title">Senior Executive Officer</p>
    </div>

    <div class="holder-arabic" lang="ar" dir="rtl">
      <p class="holder-arabic-name">خالد يوسف الرميثي</p>
      <p class="holder-arabic-title">المدير التنفيدي</p>
    </div>

    <ul class="contacts">
      <li>
        <svg class="contact-icon" viewBox="0 0 16 16" aria-hidden="true"><circle cx="8" cy="8" r="8" fill="var(--ink-light)"/><path d="M5 4.5h2l.6 2-1.1.8a5 5 0 0 0 2.2 2.2l.8-1.1 2 .6v2a1 1 0 0 1-1 1A6.5 6.5 0 0 1 4 5.5a1 1 0 0 1 1-1z" fill="var(--charcoal)"/></svg>
        <span>+9714987650</span>
      </li>
      <li>
        <svg class="contact-icon" viewBox="0 0 16 16" aria-hidden="true"><circle cx="8" cy="8" r="8" fill="var(--ink-light)"/><rect x="4" y="5.5" width="8" height="5.5" rx=".6" fill="var(--charcoal)"/><path d="M4.3 5.9 8 8.6l3.7-2.7" stroke="var(--ink-light)" stroke-width=".9" fill="none"/></svg>
        <span>krumaithi@ashbournepartners.com</span>
      </li>
      <li>
        <svg class="contact-icon" viewBox="0 0 16 16" aria-hidden="true"><circle cx="8" cy="8" r="8" fill="var(--ink-light)"/><path d="M8 3.5a3 3 0 0 1 3 3c0 2.2-3 5.8-3 5.8s-3-3.6-3-5.8a3 3 0 0 1 3-3z" fill="var(--charcoal)"/><circle cx="8" cy="6.5" r="1.1" fill="var(--ink-light)"/></svg>
        <span>Palm Terrace 07, Level 3, Office 215/12<br>HLMZ</span>
      </li>
    </ul>

    <p class="website">www.ashbournepartners.com</p>
  </section>

</body>
</html>
```